Web App, Website for Heavy Truck Roadside Assistance

We need a website designed called tolbrix.com The main aim of Tolbrix is to offer On Demand Roadside Assistance to heavy trucks/18 wheeler's in USA. I have attached the contents, with detailed instructions. The site needs to be very inviting and bright with some small colors, that would be eye popping to the viewer. I would also like to add header slider.. here is a demo of the old site... (this is just for reference ONLY) http://tolbrix.samplehost.net/app_dev.php/#!portfolio. Add photos as needed

Target Market(s)

Heavy Truck Roadside Assistance

Number of Pages Required

1 page

Font styles to use
Serif

Requirements
Must have
• sample link in the Project description
Nice to have
• use your own ideals

```html
<!DOCTYPE html>
<html lang="en">
<head>
<meta charset="utf-8">
<title>Tolbrix – Roadside Assistance in the USA</title>
<link rel="stylesheet" href="https://fonts.googleapis.com/css2?family=Open+Sans:wght@400;600;700;800&display=swap">
<style>
:root{
  --red:#d7281f;
  --red-dark:#8e1712;
  --ink:#333333;
  --muted:#6b6b6b;
  --line:#dddddd;
  --light:#f3f3f3;
  --white:#ffffff;
  --footer:#2b2b2b;
  --footer-dark:#1f1f1f;
  --map:#5f7284;
}
*{box-sizing:border-box;margin:0;padding:0}
html,body{width:1200px;height:2848px;overflow:hidden}
body{font-family:"Open Sans",Arial,sans-serif;color:var(--ink);background:var(--white);font-size:15px}
.section-title{font-weight:800;font-size:40px;letter-spacing:1px;text-align:center;text-transform:uppercase;color:var(--red)}
.rule{width:60px;height:3px;background:var(--red);margin:14px auto 0}
.btn-outline{display:inline-block;border:1px solid var(--red);color:var(--red);font-size:12px;padding:9px 20px;text-transform:uppercase;letter-spacing:.5px}
.btn-ghost{display:inline-block;border:1px solid #bbb;color:#888;font-size:12px;padding:9px 20px;text-transform:uppercase}

/* hero */
.hero{position:relative;height:600px;background:linear-gradient(160deg,#9aa7b1 0%,#5d6770 45%,#3c4148 100%);color:var(--white);overflow:hidden}
.hero-photo{position:absolute;inset:0;background:radial-gradient(ellipse at 70% 45%,#7c858d 0%,#4a5158 55%,#2d3136 100%)}
.hero-shade{position:absolute;left:0;right:0;bottom:0;height:260px;background:linear-gradient(to bottom,rgba(0,0,0,0),rgba(0,0,0,.55))}
.topbar{position:absolute;top:0;left:0;right:0;height:72px;display:flex;align-items:center;padding:0 28px;background:rgba(0,0,0,.15)}
.brand{font-weight:800;font-size:30px;letter-spacing:1px;color:var(--white);display:flex;align-items:center;gap:10px}
.brand-dot{width:14px;height:14px;background:var(--red)}
.nav{margin-left:auto;display:flex;align-items:center;gap:26px;font-size:13px}
.nav a{color:var(--white);text-decoration:none}
.nav .nav-login{border:1px solid var(--white);padding:7px 14px}
.play{position:absolute;left:568px;top:272px;width:64px;height:64px}
.hero-title{position:absolute;top:360px;left:0;right:0;text-align:center;font-weight:800;font-size:46px;letter-spacing:1px}
.hero-sub{position:absolute;top:424px;left:0;right:0;text-align:center;font-size:14px;color:#e6e6e6}
.hero-points{position:absolute;top:448px;left:0;right:0;display:flex;justify-content:center;gap:44px;font-weight:700;font-size:15px}
.hero-points span{display:flex;align-items:center;gap:8px}

/* about */
.about{height:288px;padding-top:60px;text-align:center}
.about p{width:1080px;margin:26px auto 26px;font-size:13px;line-height:1.6;color:var(--muted)}

/* how */
.how{height:332px;background:var(--light);padding-top:30px;text-align:center;border-top:1px solid var(--line)}
.steps{display:flex;justify-content:center;gap:100px;margin-top:40px}
.step{width:260px}
.step-icon{width:64px;height:64px;margin:0 auto 16px}
.step p{font-size:14px;line-height:1.5;color:var(--muted)}
.how .btn-outline{margin-top:20px}

/* locations */
.locations{height:320px;position:relative;background:linear-gradient(180deg,#6c7d8d,#54606d);color:var(--white);text-align:center;padding-top:70px}
.locations .section-title{color:var(--white)}
.locations p{width:1080px;margin:24px auto 28px;font-size:13px;line-height:1.6;color:#e9edf0}
.zip{width:310px;height:36px;margin:0 auto;background:var(--white);color:#777;font-size:13px;display:flex;align-items:center;justify-content:space-between;padding:0 14px;text-align:left}

/* blog */
.blog{height:420px;padding:48px 60px 0}
.blog-head{display:flex;align-items:center;justify-content:space-between}
.blog-head .section-title{text-align:left}
.blog-arrows{display:flex;gap:8px}
.blog-arrows span{width:24px;height:24px;border-radius:50%;background:#9a9a9a;display:flex;align-items:center;justify-content:center}
.posts{display:flex;gap:30px;margin-top:20px}
.post{width:340px}
.post-photo{height:160px}
.post p{font-size:12px;line-height:1.5;color:var(--muted);margin-top:12px}
.post .more{font-size:11px;color:var(--red);margin-top:6px;display:block}

/* work */
.work{height:340px;background:linear-gradient(100deg,#7f120e 0%,#a31c16 45%,#5b0d0a 100%);color:var(--white);text-align:center;padding-top:64px}
.work .section-title{color:var(--white)}
.work h3{font-size:20px;font-weight:600;margin-top:10px}
.work p{width:1040px;margin:14px auto 34px;font-size:13px;line-height:1.6;color:#f1dcdb}
.work-actions{display:flex;justify-content:center;gap:12px}
.work-actions span{border:1px solid var(--white);font-size:12px;padding:9px 20px;text-transform:uppercase}

/* login */
.login{height:180px;padding-top:36px;text-align:center}
.login-form{display:flex;justify-content:center;gap:10px;margin-top:34px}
.field{width:200px;height:34px;border:1px solid #ccc;font-size:12px;color:#999;display:flex;align-items:center;padding:0 10px}
.btn-red{background:var(--red);color:var(--white);font-size:12px;height:34px;padding:0 20px;display:flex;align-items:center;text-transform:uppercase}

/* contact */
.contact{height:240px;display:flex}
.contact-map{width:640px;background:linear-gradient(135deg,#e2e4e6,#c9ccd0)}
.contact-panel{flex:1;background:#ececec;padding:18px 40px}
.contact-panel h2{font-weight:400;font-size:28px;color:#555}
.contact-grid{display:grid;grid-template-columns:360px 360px;gap:12px;margin-top:16px}
.contact-grid .field{width:auto;background:var(--white);border-color:#ddd}
.contact-grid .send{background:#2a2a2a;color:var(--white);font-size:12px;display:flex;align-items:center;justify-content:center;text-transform:uppercase;height:34px}

/* footer */
.footer{height:128px;background:var(--footer);color:#bbb;font-size:12px}
.footer-top{height:56px;display:flex;align-items:center;gap:60px;padding:0 40px;border-bottom:1px solid #3a3a3a}
.footer-top span{display:flex;align-items:center;gap:8px}
.social{margin-left:auto;display:flex;gap:8px}
.social i{width:20px;height:20px;background:#555;display:block}
.footer-links{text-align:center;padding-top:16px}
.footer-links a{color:#bbb;text-decoration:none;margin:0 8px}
.copyright{text-align:center;padding-top:10px;font-size:11px;color:#888}
</style>
</head>
<body>

<header class="hero">
  <div class="hero-photo" role="img" aria-label="Photo of a heavy truck wheel being serviced on the roadside"></div>
  <div class="hero-shade"></div>
  <div class="topbar">
    <div class="brand"><span class="brand-dot"></span>TOLBRIX</div>
    <nav class="nav">
      <a href="#">About us</a><a href="#">How it works</a><a href="#">Locations covered</a><a href="#">Blog</a><a href="#">Work with us</a><a href="#">Contact</a><a href="#" class="nav-login">Servicer Login</a>
    </nav>
  </div>
  <svg class="play" viewBox="0 0 64 64"><circle cx="32" cy="32" r="30" fill="none" stroke="#fff" stroke-width="3"/><path d="M26 20 L46 32 L26 44 Z" fill="#fff"/></svg>
  <h1 class="hero-title">ROADSIDE ASSISTANCE IN THE USA</h1>
  <p class="hero-sub">Getting you back on the road fast anywhere in the USA, whether you need a quick tyre fix, a jump start or towing</p>
  <div class="hero-points">
    <span><svg width="16" height="16" viewBox="0 0 16 16"><path d="M2 8 L6 12 L14 3" fill="none" stroke="#fff" stroke-width="2.5"/></svg>Less Wait Time Means Fast Results</span>
    <span><svg width="16" height="16" viewBox="0 0 16 16"><path d="M2 8 L6 12 L14 3" fill="none" stroke="#fff" stroke-width="2.5"/></svg>100% Guarantee</span>
    <span><svg width="16" height="16" viewBox="0 0 16 16"><path d="M2 8 L6 12 L14 3" fill="none" stroke="#fff" stroke-width="2.5"/></svg>Let Us Prove It</span>
  </div>
</header>

<section class="about">
  <h2 class="section-title">About Us</h2>
  <div class="rule"></div>
  <p>Tolbrix offers on demand roadside assistance to heavy trucks and 18 wheeler operators across the USA. Driving is your time and money, and we understand how important it is for you to get reliable roadside service fast. Tolbrix provides quick service and fair rates with no hidden fees. Our innovative approach to roadside assistance means that you get back on the road sooner, without having to pay expensive subscriptions to a traditional roadside assistance service.</p>
  <span class="btn-ghost">Read more</span>
</section>

<section class="how">
  <h2 class="section-title">How It Works</h2>
  <div class="steps">
    <div class="step">
      <svg class="step-icon" viewBox="0 0 64 64"><circle cx="32" cy="32" r="29" fill="none" stroke="#d7281f" stroke-width="2"/><rect x="22" y="24" width="18" height="18" fill="none" stroke="#d7281f" stroke-width="2"/><path d="M30 36 L42 22" stroke="#d7281f" stroke-width="2.5"/></svg>
      <p>Register with Tolbrix to gain access to our services.</p>
    </div>
    <div class="step">
      <svg class="step-icon" viewBox="0 0 64 64"><circle cx="32" cy="32" r="29" fill="none" stroke="#d7281f" stroke-width="2"/><rect x="25" y="18" width="14" height="28" rx="2" fill="none" stroke="#d7281f" stroke-width="2"/><circle cx="32" cy="41" r="1.5" fill="#d7281f"/></svg>
      <p>In the event of an emergency, connect to roadside assistance instantly with our app.</p>
    </div>
    <div class="step">
      <svg class="step-icon" viewBox="0 0 64 64"><circle cx="32" cy="32" r="29" fill="none" stroke="#d7281f" stroke-width="2"/><circle cx="32" cy="32" r="12" fill="none" stroke="#d7281f" stroke-width="2"/><path d="M32 25 V32 L37 35" fill="none" stroke="#d7281f" stroke-width="2"/></svg>
      <p>Service providers respond to your needs in real time, getting you back on the road fast.</p>
    </div>
  </div>
  <span class="btn-outline">Get started now</span>
</section>

<section class="locations" role="img" aria-label="Map of the United States behind the section">
  <h2 class="section-title">Locations Covered</h2>
  <p>Tolbrix is always open to the latest updates. Fleet owners, truck drivers and independent operators can rely on our nationwide network of servicers across all major routes, from the coasts to the heartland, with more locations added every month as our coverage grows.</p>
  <div class="zip">Zip Code<svg width="10" height="6" viewBox="0 0 10 6"><path d="M0 0 L5 6 L10 0 Z" fill="#777"/></svg></div>
</section>

<section class="blog">
  <div class="blog-head">
    <h2 class="section-title">Blog</h2>
    <div class="blog-arrows">
      <span><svg width="8" height="10" viewBox="0 0 8 10"><path d="M6 1 L2 5 L6 9" fill="none" stroke="#fff" stroke-width="2"/></svg></span>
      <span><svg width="8" height="10" viewBox="0 0 8 10"><path d="M2 1 L6 5 L2 9" fill="none" stroke="#fff" stroke-width="2"/></svg></span>
    </div>
  </div>
  <div class="posts">
    <article class="post">
      <div class="post-photo" role="img" aria-label="Photo of a mechanic working on a truck" style="background:linear-gradient(135deg,#5a6f8c,#b9c2cc)"></div>
      <p>Simple tips to keep your rig road ready and avoid costly breakdowns on long hauls across the country.</p>
      <span class="more">Read more</span>
    </article>
    <article class="post">
      <div class="post-photo" role="img" aria-label="Photo of a driver beside a car on the roadside" style="background:linear-gradient(135deg,#8fae7a,#e3c6b8)"></div>
      <p>What to do in the first minutes after a breakdown so help reaches you faster and safer on the road.</p>
      <span class="more">Read more</span>
    </article>
    <article class="post">
      <div class="post-photo" role="img" aria-label="Photo of a driver sitting in a truck cab" style="background:linear-gradient(135deg,#b9b5ad,#6d6a66)"></div>
      <p>How on demand assistance is changing life for owner operators and fleets driving every single day.</p>
      <span class="more">Read more</span>
    </article>
  </div>
</section>

<section class="work" role="img" aria-label="Photo of a red truck on the highway behind the section">
  <h2 class="section-title">Work With Us</h2>
  <h3>Find Work, Get Paid, Earn More</h3>
  <p>Tolbrix is the most efficient way to find roadside work and get paid, hassle free. Join now and start earning. Our innovative app gives providers real work requests and brings your business to drivers in the area, whether you have one driver or ten.</p>
  <div class="work-actions"><span>Read more</span><span>Join now</span></div>
</section>

<section class="login">
  <h2 class="section-title">Servicer Login</h2>
  <div class="login-form">
    <div class="field">Username</div>
    <div class="field">Password</div>
    <div class="btn-red">Login</div>
  </div>
</section>

<section class="contact">
  <div class="contact-map" role="img" aria-label="World map"></div>
  <div class="contact-panel">
    <h2>Contact Us</h2>
    <div class="contact-grid">
      <div class="field">Name</div><div class="field">Email Address</div>
      <div class="field">Phone</div><div class="field">Email</div>
      <div class="field">Message</div><div class="send">Submit</div>
    </div>
  </div>
</section>

<footer class="footer">
  <div class="footer-top">
    <span><svg width="12" height="16" viewBox="0 0 12 16"><path d="M6 0 C2.7 0 0 2.6 0 5.8 C0 10 6 16 6 16 S12 10 12 5.8 C12 2.6 9.3 0 6 0 Z" fill="#bbb"/><circle cx="6" cy="6" r="2" fill="#2b2b2b"/></svg>10 Building name, Street Name, City, Zip code</span>
    <span><svg width="14" height="14" viewBox="0 0 14 14"><path d="M3 1 L5 1 L6 4 L4.5 5 C5.5 7 7 8.5 9 9.5 L10 8 L13 9 L13 11 C13 12 12 13 11 13 C5.5 13 1 8.5 1 3 C1 2 2 1 3 1 Z" fill="#bbb"/></svg>Call Now: 000 000 0000</span>
    <span><svg width="16" height="12" viewBox="0 0 16 12"><rect x="0.5" y="0.5" width="15" height="11" fill="none" stroke="#bbb"/><path d="M1 1 L8 7 L15 1" fill="none" stroke="#bbb"/></svg>Email: info@tolbrix.com</span>
    <div class="social"><i></i><i></i><i></i><i></i></div>
  </div>
  <div class="footer-links">
    <a href="#">Home</a>|<a href="#">About us</a>|<a href="#">How it works</a>|<a href="#">Locations Covered</a>|<a href="#">Blog</a>|<a href="#">Work with us</a>|<a href="#">Contact</a>|<a href="#">Servicer Login</a>
  </div>
  <div class="copyright">Copyright © 2016 Tolbrix.com</div>
</footer>

</body>
</html>
```